Design letter head and business card

Hello,

you should design a business card and letter paper for Wolkenfalke Marketing. In German we write this word with K insteat of C.

Company does not have a logo. But in general, we write Wolkenfalke Marketing in 2 lines.
First line red: WOLKENFALKE
Second line gray: MARKETING

Red (or wine red) and Gray / Black are our favorite colors.

Company slogan: "Next Level Online Marketing".

Company offers SEO, SEM, SEA, AdWords, Conversion Optimization, Online Markting Consulting ...

The website is old, please do not use this as base for your task.

German letter paper sizes:
Viawable Dimensions : 210 x 297 mm
Needed file dimensions: 212 x 299 mm

Informations to include:

Address:
Wolkenfalke Marketing GmbH
Lindenweg 23
71384 Weinstadt
Germany

Geschäftsführer | CEO: Dietrich Ronnau

Phone: +49 (0) 7151 482 67 05

Fax: +49 (0) 7151 482 67 88

Mail: info@wolkenfalke-marketing.de

Web: www.wolkenfalke-marketing.de

Amtsgericht Suttgart, HRB 736402

Bank: Sonnfelder Bank
IBAN: DE139817325500XXXXXXXX
BIC: GENODES1QTR

Thanks

Dietrich

Target Market(s)

People who likes to win the online marketing game.

Industry/Entity Type

Business

Contact Information for Business Card

Here is the personal text on the card:

Name:
Dietrich Ronnau

Title:
Geschäftsführer | CEO

Address:
Wolkenfalke Marketing GmbH
Lindenweg 23
71384 Weinstadt
Germany

Phone:
+49 (0) 7151 482 67 05

Fax:
+49 (0) 7151 482 67 88

Mail:
ronnau@wolkenfalke-marketing.de

Web:
www.wolkenfalke-marketing.de

Business Card:
Viewable Dimensions: 85 x 55 mm
Needed file dimensions: 87 x 57mm

Font styles to use
Sans Serif

Requirements
Nice to have
• It would be great to see the dynamics of a helicopter.

```html
<!DOCTYPE html>
<html lang="en">
<head>
<meta charset="utf-8">
<title>Wolkenfalke Marketing – Business Card</title>
<link href="https://fonts.googleapis.com/css2?family=Lato:wght@400;700&family=Lora&display=swap" rel="stylesheet">
<style>
  :root {
    --page-bg: #ecebea;
    --brand-red: #c8202a;
    --card-dark: #3b3b3d;
    --card-dark-light: #4a4a4c;
    --card-white: #ffffff;
    --card-white-shade: #e9e9ea;
    --strip-gray: #8e8e90;
    --title-salmon: #f4a79a;
    --tagline-gray: #858587;
    --text-white: #ffffff;
  }
  * { box-sizing: border-box; margin: 0; padding: 0; }
  html, body { width: 1200px; height: 900px; overflow: hidden; }
  body {
    background: var(--page-bg);
    font-family: "Lato", Arial, sans-serif;
    position: relative;
  }
  .card {
    position: absolute;
    width: 640px;
    height: 366px;
    overflow: hidden;
    box-shadow: 0 10px 28px rgba(0,0,0,0.18);
  }

  /* Company name, set as plain text */
  .company-name {
    font-family: "Lato", Arial, sans-serif;
    font-weight: 400;
    font-size: 42px;
    line-height: 1.1;
    color: var(--brand-red);
    white-space: nowrap;
  }

  /* Back side */
  .card-back {
    left: 90px; top: 60px;
    background: radial-gradient(ellipse at 50% 45%, var(--card-dark-light) 0%, var(--card-dark) 70%);
  }
  .card-back .company-name {
    position: absolute;
    left: 0; right: 0; top: 128px;
    text-align: center;
  }
  .tagline {
    position: absolute;
    left: 0; right: 0; top: 190px;
    text-align: center;
    font-family: "Lora", Georgia, serif;
    color: var(--tagline-gray);
    font-size: 22px;
    letter-spacing: 0.4px;
  }

  /* Front side */
  .card-front {
    left: 470px; top: 470px;
    background: linear-gradient(160deg, var(--card-white) 40%, var(--card-white-shade) 100%);
  }
  .card-front .company-name {
    position: absolute;
    right: 60px; top: 96px;
  }
  .info-band {
    position: absolute;
    left: 0; right: 0; top: 196px; height: 128px;
    background: var(--brand-red);
  }
  .bottom-strip {
    position: absolute;
    left: 0; right: 0; bottom: 0; height: 42px;
    background: var(--strip-gray);
  }
  .person {
    position: absolute;
    right: 316px; top: 214px;
    text-align: right;
    color: var(--text-white);
  }
  .person-name { font-size: 24px; font-weight: 700; line-height: 1.1; }
  .person-title { font-size: 16px; color: var(--title-salmon); line-height: 1.4; margin-bottom: 6px; }
  .person-address { font-size: 18px; line-height: 1.3; }
  .contact-list {
    position: absolute;
    left: 350px; top: 206px;
    list-style: none;
    color: var(--text-white);
    font-size: 16px;
  }
  .contact-list li {
    display: flex;
    align-items: center;
    gap: 8px;
    height: 25px;
  }
  .contact-icon { width: 17px; height: 17px; flex: none; }
</style>
</head>
<body>

<section class="card card-back" aria-label="Business card back">
  <p class="company-name">Wolkenfalke Marketing</p>
  <p class="tagline">Next Level Online Marketing</p>
</section>

<section class="card card-front" aria-label="Business card front">
  <p class="company-name">Wolkenfalke Marketing</p>
  <div class="info-band"></div>
  <div class="bottom-strip"></div>

  <div class="person">
    <p class="person-name">John Smith</p>
    <p class="person-title">Managing Director</p>
    <p class="person-address">1234, Address GoesHere<br>Country, 12345</p>
  </div>

  <ul class="contact-list">
    <li>
      <svg class="contact-icon" viewBox="0 0 17 17" aria-hidden="true">
        <rect width="17" height="17" rx="3" fill="#fff"/>
        <path d="M4 6 Q4 4 6 4 L11 4 Q13 4 13 6 L11 7 L10 6 L7 6 L6 7 Z" fill="#c8202a"/>
        <rect x="5" y="8" width="7" height="5" rx="1" fill="#c8202a"/>
      </svg>
      <span>123-456-7890</span>
    </li>
    <li>
      <svg class="contact-icon" viewBox="0 0 17 17" aria-hidden="true">
        <rect width="17" height="17" rx="3" fill="#fff"/>
        <rect x="4" y="6" width="9" height="7" rx="1" fill="#c8202a"/>
        <rect x="6" y="3.5" width="5" height="3" fill="#c8202a"/>
        <rect x="6" y="9" width="5" height="1.5" fill="#fff"/>
      </svg>
      <span>123-456-7890</span>
    </li>
    <li>
      <svg class="contact-icon" viewBox="0 0 17 17" aria-hidden="true">
        <rect width="17" height="17" rx="3" fill="#fff"/>
        <rect x="3.5" y="5" width="10" height="7" fill="#c8202a"/>
        <path d="M3.5 5 L8.5 9 L13.5 5" fill="none" stroke="#fff" stroke-width="1.2"/>
      </svg>
      <span>info@youremail.com</span>
    </li>
    <li>
      <svg class="contact-icon" viewBox="0 0 17 17" aria-hidden="true">
        <rect width="17" height="17" rx="3" fill="#fff"/>
        <path d="M7 10 L10 7 M6 8.5 L4.8 9.7 a2 2 0 0 0 2.8 2.8 L8.8 11.3 M8.5 6 L9.7 4.8 a2 2 0 0 1 2.8 2.8 L11.3 8.8" fill="none" stroke="#c8202a" stroke-width="1.5" stroke-linecap="round"/>
      </svg>
      <span>www.yourweb.com</span>
    </li>
  </ul>
</section>

</body>
</html>
```